TVRB web site redesign

Meridale Linkworks Provisioning service (TVRB) is a diverse technology company specialising in design and installation of fibre optics, network convergence and building services, for commercial clients in Australia, we required a new design of our website to attract new clients, generate sales leads, and provide information about our services to the market. The site and should have a new technology look and feel and be designed in word press. our branding colour is blue.

Target Market(s)

New developments, Construction organisations, Commercial end users, IT managers, Consultants.

Industry/Entity Type

It Company

Number of Pages Required

5+ page

Font styles to use
Sans Serif

Colors
0292cd
3176b5

Requirements
Must have
• key pages.
• Home page with some sizzle, automated pictures running through, I like the look of this competitor website http://www.lumacrest.com.au/ good clean menus and easy to navigate.
• Services page our key services are Fibre optics, Security, Building services,Electrical. I would like the same page layout (Design) for all our services, with a find out more link on each page, manly picture driven with text around our key messaging.
• About us page with space for company profile and directors pictures, bio and contact information.
• Certifications / Accreditations page with have over 20 certifications on different products from suppliers, and a number of licences from governing bodies.
• Current and past projects page with case studies and customer outcomes
• Contact us page with options around what services they require more information on, please keep in mind the site is around generating sales Leeds and being seen as an industry expert.
Nice to have
• RSS feeds, Linked in link, to be placed within the design, Consistent TVRB branding,Same colour blue as our logo Document library for education information, white papers, presentations etc,
• a new technology look and feel, mobile friendly.
Should not have
• boring layout, move away from our cuurent website http://www.tvrbgroup.com.au/
• no e eCommerce store required.

```html
<!DOCTYPE html>
<html lang="en">
<head>
<meta charset="utf-8">
<title>TVRB – Communications Integration</title>
<link href="https://fonts.googleapis.com/css2?family=Open+Sans:ital,wght@0,400;0,600;0,700;1,400&family=Great+Vibes&family=Lora:ital,wght@1,400;1,700&display=swap" rel="stylesheet">
<style>
:root{
  --blue:#0292cd;
  --blue-dark:#3176b5;
  --ink:#333;
  --muted:#666;
  --line:#d5d5d5;
  --topbar:#151515;
  --footer:#222;
  --footer-deep:#161616;
  --white:#fff;
}
*{box-sizing:border-box;margin:0;padding:0}
html,body{width:1200px;height:2760px;overflow:hidden}
body{font-family:"Open Sans",Arial,sans-serif;color:var(--ink);background:var(--white);font-size:13px;line-height:1.6}
a{color:inherit;text-decoration:none}

.topbar{height:24px;background:var(--topbar);color:#bbb;font-size:10px;display:flex;align-items:center;justify-content:space-between;padding:0 40px}
.topbar .contact{display:flex;gap:18px}
.topbar .contact span{display:flex;align-items:center;gap:5px}

.header{height:78px;display:flex;align-items:center;justify-content:space-between;padding:0 40px}
.brand{display:flex;align-items:center;gap:10px;font-weight:700;font-size:30px;color:var(--blue);letter-spacing:1px}
.brand .mark{width:26px;height:26px;background:var(--blue)}
.nav{display:flex;height:78px}
.nav a{display:flex;align-items:center;padding:0 15px;font-size:13px;color:#444}
.nav a.active{background:var(--blue);color:var(--white)}

.hero{position:relative;height:460px;background:linear-gradient(100deg,#6b7a86 0%,#aeb8bf 40%,#e8ecef 70%,#c9d1d7 100%)}
.hero-caption{position:absolute;left:130px;top:200px;width:620px;display:flex;flex-direction:column;align-items:flex-start}
.hero-caption h1{font-family:"Lora",Georgia,serif;font-style:italic;font-weight:700;font-size:24px;line-height:1.4;color:var(--white);background:rgba(20,40,60,.75);padding:10px 18px;white-space:nowrap}
.hero-caption p{background:rgba(2,146,205,.85);color:var(--white);font-size:13px;line-height:1.5;padding:8px 18px}
.btn{display:inline-block;background:var(--blue);color:var(--white);font-size:12px;font-weight:700;padding:9px 18px;letter-spacing:.5px}
.hero-caption .btn{margin-top:16px}

.script-title{font-family:"Great Vibes",cursive;font-size:48px;color:var(--blue-dark);text-align:center;display:flex;align-items:center;justify-content:center;gap:20px}
.script-title::before,.script-title::after{content:"";width:150px;height:1px;background:var(--line)}

.about{height:330px;padding:40px 100px 0}
.about-body{display:flex;gap:30px;margin-top:22px}
.about-logo{flex:0 0 200px;display:flex;align-items:center;gap:10px;font-weight:700;font-size:40px;color:var(--blue)}
.about-logo .mark{width:34px;height:34px;background:var(--blue)}
.about-body p{color:var(--muted);font-size:13px}
.about-body .btn{margin-top:14px}

.services{height:540px;background:linear-gradient(180deg,var(--blue) 0%,var(--blue-dark) 100%);padding-top:40px}
.services .script-title{color:var(--white)}
.services .script-title::before,.services .script-title::after{background:rgba(255,255,255,.5)}
.service-grid{display:flex;justify-content:center;gap:60px;margin-top:36px}
.service{width:200px;text-align:center;color:var(--white)}
.service .photo{position:relative;width:190px;height:190px;border-radius:50%;border:5px solid var(--white);margin:0 auto}
.service .photo .overlay{position:absolute;inset:0;border-radius:50%;background:rgba(2,146,205,.8);display:flex;align-items:center;justify-content:center;font-weight:700;font-size:13px}
.service h3{font-size:16px;font-weight:600;margin-top:20px}
.service p{font-size:11px;line-height:1.5;opacity:.9;margin-top:6px}
.ph-fibre{background:radial-gradient(circle,#7ad0f0,#1c3e6e)}
.ph-security{background:radial-gradient(circle,#e8e8e8,#8a8f96)}
.ph-building{background:linear-gradient(180deg,#a9cbe6,#5c6f80)}
.ph-electrical{background:radial-gradient(circle,#f0a050,#a84f1c)}

.projects{height:858px;padding:40px 40px 0}
.project-cols{display:flex;gap:40px;margin-top:24px}
.col{flex:1}
.col h2{font-family:"Lora",Georgia,serif;font-style:italic;font-weight:700;font-size:24px;color:var(--ink);border-bottom:1px solid var(--line);padding-bottom:8px;margin-bottom:20px}
.past-item{display:flex;gap:18px;margin-bottom:16px}
.past-item .thumb{flex:0 0 200px;height:150px;background:linear-gradient(160deg,#9fc4d8,#4c6e4c)}
.item-title{color:var(--blue);font-size:16px;font-weight:600;margin-bottom:6px}
.item-text{font-size:11px;color:var(--muted);line-height:1.5}
.more{display:block;text-align:right;font-size:11px;font-weight:700;color:var(--blue-dark);margin-top:6px}
.current .thumb{height:260px;background:linear-gradient(170deg,#cfe0ea 0%,#8fb07a 50%,#5f7d4c 100%)}
.current .item-title{margin-top:16px}

.footer{height:430px;background:var(--footer);color:#aaa;padding:40px 40px 0;position:relative}
.footer-cols{display:flex;gap:40px}
.footer h4{font-family:"Lora",Georgia,serif;font-style:italic;font-size:22px;color:var(--white);margin-bottom:18px}
.f-contact{flex:0 0 340px}
.f-contact p{font-size:11px;margin-bottom:10px}
.field-row{display:flex;gap:8px;margin-bottom:8px}
.field{flex:1;height:30px;background:var(--white);font-size:10px;color:#999;padding:7px 8px}
.field.area{height:100px}
.submit{display:inline-block;background:var(--white);color:var(--ink);font-size:10px;font-weight:700;padding:6px 14px;margin-top:4px}
.f-links{flex:1}
.f-links li{list-style:none;font-size:11px;padding:8px 0;border-bottom:1px solid #333}
.tweet{display:flex;gap:10px;font-size:11px;margin-bottom:14px}
.tweet .dot{flex:0 0 14px;height:14px;background:var(--blue);border-radius:50%;margin-top:2px}
.tweet small{display:block;color:#777;font-size:10px}
.copyright{position:absolute;left:0;right:0;bottom:0;height:40px;background:var(--footer-deep);color:#777;font-size:10px;text-align:center;line-height:40px}
</style>
</head>
<body>

<div class="topbar">
  <span>Welcome, user</span>
  <div class="contact">
    <span><svg width="10" height="10" viewBox="0 0 10 10"><path d="M2 1l2 2-1 1.5c.6 1.2 1.3 1.9 2.5 2.5L7 6l2 2-1.5 1.5C4 9 1 6 .5 2.5z" fill="#bbb"/></svg>1300 555 014</span>
    <span><svg width="11" height="9" viewBox="0 0 11 9"><rect x=".5" y=".5" width="10" height="8" fill="none" stroke="#bbb"/><path d="M.5.5l5 4 5-4" fill="none" stroke="#bbb"/></svg>info@tvrbgroup.com.au</span>
  </div>
</div>

<header class="header">
  <div class="brand"><span class="mark"></span>TVRB</div>
  <nav class="nav">
    <a class="active" href="#">Home</a><a href="#">About Us</a><a href="#">Services</a><a href="#">Commercial</a><a href="#">SIP</a><a href="#">Recent Projects</a><a href="#">Contact Us</a><a href="#">Blog</a>
  </nav>
</header>

<section class="hero" role="img" aria-label="Photo of a businessman holding a laptop in front of a server room">
  <div class="hero-caption">
    <h1>TVRB Is A Communications Integration Company</h1>
    <p>Incorporating The Expertise Of Data And Fibre Optic Communication,<br>ICT And Low Voltage Systems, Security And Application Services</p>
    <a class="btn" href="#">READ MORE</a>
  </div>
</section>

<section class="about">
  <h2 class="script-title">About Us</h2>
  <div class="about-body">
    <div class="about-logo"><span class="mark"></span>TVRB</div>
    <div>
      <p>TVRB is a diversified technology company, 100% Australian owned and operated; we provide Communications, Electrical, Security &amp; ICT services for residential and commercial customers. With over 100 years of combined industry knowledge we pride ourselves on innovative solutions that utilise technology advancements which deliver on our customer's expectations.</p>
      <a class="btn" href="#">LEARN MORE</a>
    </div>
  </div>
</section>

<section class="services">
  <h2 class="script-title">Our Service</h2>
  <div class="service-grid">
    <div class="service">
      <div class="photo ph-fibre" role="img" aria-label="Photo of glowing fibre optic strands"><span class="overlay">READ MORE</span></div>
      <h3>Fibre Optics</h3>
      <p>The TVRB has highly trained and proficient engineers, technicians and project managers to ensure that we achieve a high level.</p>
    </div>
    <div class="service">
      <div class="photo ph-security" role="img" aria-label="Photo of security cameras on a wall"></div>
      <h3>Security</h3>
      <p>The TVRB range of IP CCTV cameras and platforms allows you to keep current with technology advancements such as video.</p>
    </div>
    <div class="service">
      <div class="photo ph-building" role="img" aria-label="Photo of a modern commercial building"></div>
      <h3>Building Services</h3>
      <p>The TVRB has highly trained and proficient engineers, technicians and project managers to ensure that we achieve a high level.</p>
    </div>
    <div class="service">
      <div class="photo ph-electrical" role="img" aria-label="Photo of an electrical switchboard"></div>
      <h3>Electrical</h3>
      <p>TVRB services are the design, installation, commissioning and maintenance of a wide range of electrical systems, including.</p>
    </div>
  </div>
</section>

<section class="projects">
  <h2 class="script-title">Our Projects</h2>
  <div class="project-cols">
    <div class="col">
      <h2>Past projects</h2>
      <div class="past-item">
        <div class="thumb" role="img" aria-label="Photo of a tall green apartment tower"></div>
        <div>
          <div class="item-title">Harbourline Central</div>
          <p class="item-text">Harbourton Central Park occupies nearly six hectares of the southern Harbourton CBD, defining Harbourton's 'downtown'. Central Park is the former brewery site between Wattle Road and the old Larkfield warehouse district.</p>
        </div>
      </div>
      <p class="item-text">The site includes the protection of heritage buildings, new parklands and community facilities and substantial upgrades to urban infrastructure. The masterplan also allows for the development of approximately 255,000 sqm of residential.</p>
      <a class="more" href="#">READ MORE ➞</a>
      <div class="past-item" style="margin-top:22px">
        <div class="thumb" role="img" aria-label="Photo of a tall green apartment tower"></div>
        <div>
          <div class="item-title">Harbourline Central</div>
          <p class="item-text">Harbourton Central Park occupies nearly six hectares of the southern Harbourton CBD, defining Harbourton's 'downtown'. Central Park is the former brewery site between Wattle Road and the old Larkfield warehouse district.</p>
        </div>
      </div>
      <p class="item-text">The site includes the protection of heritage buildings, new parklands and community facilities and substantial upgrades to urban infrastructure. The masterplan also allows for the development of approximately 255,000 sqm of residential.</p>
      <a class="more" href="#">READ MORE ➞</a>
    </div>
    <div class="col current">
      <h2>Current Projects</h2>
      <div class="thumb" role="img" aria-label="Aerial rendering of a new residential valley development"></div>
      <div class="item-title">Kestrel Valley Telecommunications Backhaul</div>
      <p class="item-text">The installation of fibre optic trunk lines for Kestrel Valley, a new development of over ten thousand homes. The installation of 4 kilometres of telecommunications pit and pipe infrastructure from Swanbank Road through to Walker Road, by means of open trench and directional drilling.</p>
      <p class="item-text" style="margin-top:8px">Once all principal installations were complete, 4.5 kilometres of fibre cabling was installed along the route, which will be connected when the development is ready.</p>
      <a class="more" href="#">READ MORE ➞</a>
    </div>
  </div>
</section>

<footer class="footer">
  <div class="footer-cols">
    <div class="f-contact">
      <h4>Contact TVRB</h4>
      <p>Please contact us on 1300 555 014 or fill out below.</p>
      <div class="field-row"><div class="field">First Name</div><div class="field">Last Name</div></div>
      <div class="field-row"><div class="field">Email Address</div></div>
      <div class="field-row"><div class="field">Contact Phone</div></div>
      <div class="field-row"><div class="field area">How can we help you?</div></div>
      <span class="submit">SUBMIT</span>
    </div>
    <div class="f-links">
      <h4>My Account</h4>
      <ul><li>My Account</li><li>Sign In</li><li>Order Status</li><li>My Cart</li><li>My Wishlist</li></ul>
    </div>
    <div class="f-links">
      <h4>Information</h4>
      <ul><li>About Us</li><li>Services</li><li>SIP</li><li>Recent Projects</li><li>Contact Us</li><li>Blog</li></ul>
    </div>
    <div class="f-links">
      <h4>Latest Tweets</h4>
      <div class="tweet"><span class="dot"></span><div>New fibre rollout stage complete. tvrb.link/n3k8<small>5 hours ago</small></div></div>
      <div class="tweet"><span class="dot"></span><div>New fibre rollout stage complete. tvrb.link/n3k8<small>5 hours ago</small></div></div>
      <div class="tweet"><span class="dot"></span><div>New fibre rollout stage complete. tvrb.link/n3k8<small>5 hours ago</small></div></div>
    </div>
  </div>
  <div class="copyright">Copyright © 2024 TVRB Group. All Rights Reserved. Sitemap</div>
</footer>

</body>
</html>
```